Document Processing Services and Solutions for School Systems

I am looking to design a brochure for both Digital and Paper use. I can supply the written content. Would be looking for an overall design of the brochure with provided content worked into it.

```html
<!DOCTYPE html>
<html lang="en">
<head>
<meta charset="UTF-8">
<title>Keystone Docworks – School Document Management</title>
<link rel="stylesheet" href="https://fonts.googleapis.com/css2?family=Sora:wght@400;600;700&display=swap">
<style>
  :root {
    --brand-blue: #2e3192;
    --brand-blue-deep: #1d2766;
    --brand-gold: #c99a00;
    --brand-gold-bright: #d4a20a;
    --ink: #35353f;
    --ink-dark: #1f1f2a;
    --paper: #ffffff;
  }
  * { box-sizing: border-box; margin: 0; padding: 0; }
  html, body { width: 904px; height: 1200px; overflow: hidden; background: var(--paper); }
  body { font-family: "Sora", sans-serif; color: var(--ink); letter-spacing: -0.02em; }
  .flyer { position: relative; width: 904px; height: 1200px; background: var(--paper); }
  .shapes { position: absolute; inset: 0; width: 904px; height: 1200px; pointer-events: none; }

  /* Hero */
  .hero {
    position: absolute; left: 33px; top: 33px; width: 838px; height: 320px;
    border-radius: 10px; overflow: hidden;
    background: linear-gradient(90deg, #2c3194 0%, #2d3296 40%, #2a3a8e 62%, #1c2b60 100%);
  }
  .hero-photo {
    position: absolute; right: 0; top: 0; width: 440px; height: 320px;
    background:
      radial-gradient(circle at 52% 40%, rgba(70,120,230,0.85) 0 12%, rgba(70,120,230,0) 26%),
      linear-gradient(90deg, rgba(44,49,148,0) 0%, rgba(60,84,160,0.55) 35%, rgba(110,120,150,0.55) 70%, rgba(40,50,90,0.8) 100%);
  }
  .brand { position: absolute; left: 36px; top: 52px; display: flex; align-items: center; gap: 8px; }
  .brand-mark { width: 10px; height: 10px; background: var(--brand-gold-bright); }
  .brand-name { color: var(--paper); font-weight: 600; font-size: 19px; letter-spacing: 0; }
  .hero-title { position: absolute; left: 36px; top: 116px; color: var(--paper); font-weight: 700; font-size: 42px; letter-spacing: -0.03em; line-height: 1; }
  .hero-sub { position: absolute; left: 36px; top: 168px; color: var(--paper); font-size: 27px; line-height: 1; }
  .hero-band {
    position: absolute; left: 31px; top: 209px; width: 513px; height: 53px;
    background: var(--brand-gold); border-radius: 6px;
    color: var(--paper); font-weight: 700; font-size: 33px; line-height: 53px; padding-left: 12px; letter-spacing: -0.035em;
  }
  .hero-tag { position: absolute; left: 36px; top: 270px; color: var(--paper); font-weight: 600; font-size: 19px; }

  /* Intro */
  .intro { position: absolute; left: 69px; top: 392px; width: 380px; font-size: 14.6px; line-height: 20px; }

  /* Why choose */
  .why { position: absolute; left: 510px; top: 380px; width: 350px; }
  .why-title { color: var(--brand-gold); font-weight: 700; font-size: 25px; letter-spacing: -0.03em; }
  .why-lead { margin-top: 12px; color: var(--ink-dark); font-weight: 600; font-size: 14.6px; line-height: 20px; }
  .why-list { list-style: none; margin-top: 14px; }
  .why-list li { position: relative; padding-left: 27px; font-size: 14.6px; line-height: 20px; margin-bottom: 11px; }
  .why-list svg { position: absolute; left: 0; top: 5px; width: 12px; height: 12px; }

  /* Services */
  .services-title { position: absolute; left: 209px; top: 576px; width: 250px; text-align: center; color: var(--paper); font-weight: 600; font-size: 25px; }
  .services { position: absolute; left: 54px; top: 647px; width: 380px; }
  .service + .service { margin-top: 16px; }
  .service-head { display: flex; align-items: flex-start; gap: 9px; color: var(--brand-blue); font-weight: 700; font-size: 14.6px; line-height: 18px; }
  .service-head svg { width: 15px; height: 15px; margin-top: 2px; flex: none; }
  .service-list { list-style: none; margin-top: 8px; }
  .service-list li { position: relative; padding-left: 25px; font-size: 12px; line-height: 16px; margin-bottom: 10px; }
  .service-list li:last-child { margin-bottom: 0; }
  .service-list svg { position: absolute; left: 3px; top: 3px; width: 11px; height: 11px; }

  /* Get started */
  .illustration {
    position: absolute; left: 605px; top: 660px; width: 225px; height: 172px; border-radius: 14px;
    background: radial-gradient(circle at 62% 58%, #5a86f0 0 18%, rgba(90,134,240,0) 32%), linear-gradient(160deg, #a9bff8 0%, #6d93f2 55%, #e6ecfb 100%);
  }
  .start-title { position: absolute; left: 480px; top: 764px; color: var(--brand-blue); font-weight: 600; font-size: 20.5px; line-height: 25px; }
  .start-copy { position: absolute; left: 480px; top: 818px; width: 390px; font-size: 14.6px; line-height: 20px; }
  .contact { position: absolute; left: 522px; top: 945px; list-style: none; color: var(--paper); font-size: 15.5px; font-weight: 600; }
  .contact li { display: flex; align-items: center; gap: 16px; height: 23px; }
  .contact svg { width: 14px; height: 14px; flex: none; }
</style>
</head>
<body>
<main class="flyer">
  <svg class="shapes" viewBox="0 0 904 1200" aria-hidden="true">
    <path d="M209 575 L63 575 Q33 575 33 605 L33 1131 Q33 1161 63 1161 L422 1161 Q452 1161 452 1131 L452 715 Q452 690 410 666" fill="none" stroke="#c99a00" stroke-width="1"/>
    <path d="M229 549 L439 549 Q459 549 459 569 L459 655 Q459 675 439 675 L385 675 Q355 673 325 655 Q285 632 245 626 Q209 620 209 595 L209 569 Q209 549 229 549 Z" fill="#2e3192"/>
    <path d="M437 630 L406 630 M406 630 L416 620 M406 630 L416 640" stroke="#fff" stroke-width="2.4" fill="none" stroke-linecap="round"/>
    <path d="M528 922 L838 922 Q871 922 871 955 L871 1128 Q871 1161 838 1161 L680 1161 Q640 1161 600 1140 Q560 1120 525 1105 Q486 1088 486 1050 L486 962 Q486 922 528 922 Z" fill="#cc9a00"/>
    <path d="M760 1118 L738 1096 M738 1096 L738 1110 M738 1096 L752 1096" stroke="#fff" stroke-width="2.2" fill="none" stroke-linecap="round"/>
  </svg>

  <header class="hero">
    <div class="hero-photo" role="img" aria-label="Photo of hands typing on a laptop with floating digital document and folder icons"></div>
    <div class="brand"><span class="brand-mark"></span><span class="brand-name">Keystone Docworks Inc</span></div>
    <h1 class="hero-title">Transform</h1>
    <p class="hero-sub">Your School’s</p>
    <p class="hero-band">Document Management</p>
    <p class="hero-tag">with Our Comprehensive Solutions</p>
  </header>

  <p class="intro">Managing school documents efficiently is crucial for smooth operations, compliance, and productivity. Our document processing services provide innovative solutions tailored for educational institutions, ensuring secure and seamless document and data handling.</p>

  <section class="why">
    <h2 class="why-title">Why Choose Us?</h2>
    <p class="why-lead">Increased Efficiency – Save time with digital workflows and instant document retrieval.</p>
    <ul class="why-list">
      <li><svg viewBox="0 0 12 12"><path d="M1 6.5 L4.5 10 L11 1.5" fill="none" stroke="#2e3192" stroke-width="1.8"/></svg>Enhanced Security – Protect sensitive student and faculty information.</li>
      <li><svg viewBox="0 0 12 12"><path d="M1 6.5 L4.5 10 L11 1.5" fill="none" stroke="#2e3192" stroke-width="1.8"/></svg>Cost Savings – Reduce paper, printing, and storage costs.</li>
      <li><svg viewBox="0 0 12 12"><path d="M1 6.5 L4.5 10 L11 1.5" fill="none" stroke="#2e3192" stroke-width="1.8"/></svg>Eco-Friendly – Minimize your school’s carbon footprint by going digital.</li>
    </ul>
  </section>

  <h2 class="services-title">Our Services</h2>
  <section class="services">
    <div class="service">
      <h3 class="service-head"><svg viewBox="0 0 15 15"><path d="M1 4V1h3M11 1h3v3M14 11v3h-3M4 14H1v-3" fill="none" stroke="#c99a00" stroke-width="1.4"/><rect x="4" y="4" width="7" height="7" fill="#2e3192"/></svg><span>Document Scanning<br>&amp; Conversion</span></h3>
      <ul class="service-list">
        <li><svg viewBox="0 0 12 12"><path d="M1 6.5 L4.5 10 L11 1.5" fill="none" stroke="#c99a00" stroke-width="1.8"/></svg>Convert paper records into digital formats for easy access and storage.</li>
        <li><svg viewBox="0 0 12 12"><path d="M1 6.5 L4.5 10 L11 1.5" fill="none" stroke="#c99a00" stroke-width="1.8"/></svg>High-speed scanning for student records, administrative files, and historical archives.</li>
        <li><svg viewBox="0 0 12 12"><path d="M1 6.5 L4.5 10 L11 1.5" fill="none" stroke="#c99a00" stroke-width="1.8"/></svg>OCR (Optical Character Recognition) for searchable and editable documents.</li>
      </ul>
    </div>
    <div class="service">
      <h3 class="service-head"><svg viewBox="0 0 15 15"><path d="M3.5 10.5a3 3 0 0 1 0-6a4 4 0 0 1 7.5-.5a3 3 0 0 1 .5 6.5z" fill="#2e3192"/><path d="M5 11v3M7.5 11v3M10 11v3" stroke="#2e3192" stroke-width="1.2"/></svg><span>Cloud-Based Document Management</span></h3>
      <ul class="service-list">
        <li><svg viewBox="0 0 12 12"><path d="M1 6.5 L4.5 10 L11 1.5" fill="none" stroke="#c99a00" stroke-width="1.8"/></svg>Secure, centralized document storage accessible from anywhere.</li>
        <li><svg viewBox="0 0 12 12"><path d="M1 6.5 L4.5 10 L11 1.5" fill="none" stroke="#c99a00" stroke-width="1.8"/></svg>Role-based access controls for administrators, teachers, and staff.</li>
        <li><svg viewBox="0 0 12 12"><path d="M1 6.5 L4.5 10 L11 1.5" fill="none" stroke="#c99a00" stroke-width="1.8"/></svg>Automated backups and compliance with educational data security standards.</li>
      </ul>
    </div>
    <div class="service">
      <h3 class="service-head"><svg viewBox="0 0 15 15"><rect x="1" y="1" width="6" height="5" fill="#c99a00"/><rect x="8" y="9" width="6" height="5" fill="#2e3192"/><path d="M4 7v4h3M10 6V3H8" fill="none" stroke="#2e3192" stroke-width="1.2"/></svg><span>Workflow Automation</span></h3>
      <ul class="service-list">
        <li><svg viewBox="0 0 12 12"><path d="M1 6.5 L4.5 10 L11 1.5" fill="none" stroke="#c99a00" stroke-width="1.8"/></svg>Digitize and streamline approval processes for enrollment, transcripts, and HR forms.</li>
        <li><svg viewBox="0 0 12 12"><path d="M1 6.5 L4.5 10 L11 1.5" fill="none" stroke="#c99a00" stroke-width="1.8"/></svg>Reduce paperwork and improve efficiency with automated workflows.</li>
        <li><svg viewBox="0 0 12 12"><path d="M1 6.5 L4.5 10 L11 1.5" fill="none" stroke="#c99a00" stroke-width="1.8"/></svg>Integration capable with existing school management systems.</li>
      </ul>
    </div>
  </section>

  <div class="illustration" role="img" aria-label="Illustration of a digital document with a magnifying glass"></div>
  <h2 class="start-title">Get Started<br>Today!</h2>
  <p class="start-copy">Let us help you modernize your document processing system. Contact us for a free consultation and discover how our solutions can transform your school's document management.</p>

  <ul class="contact">
    <li><svg viewBox="0 0 14 14"><path d="M2 1h3l1.5 3.5-2 1.3a8 8 0 0 0 3.7 3.7l1.3-2L13 9v3a1 1 0 0 1-1 1A11 11 0 0 1 1 2a1 1 0 0 1 1-1z" fill="#fff"/></svg>555-014-2290</li>
    <li><svg viewBox="0 0 14 14"><rect x="1" y="3" width="12" height="8.5" rx="1" fill="#fff"/><path d="M1.5 3.5 7 8l5.5-4.5" fill="none" stroke="#cc9a00" stroke-width="1.2"/></svg>hello@keystonedocs.com</li>
    <li><svg viewBox="0 0 14 14"><path d="M3 1v11l3-3 2 4.5 1.6-.7-2-4.4H12z" fill="#fff"/></svg>keystonedocs.com</li>
  </ul>
</main>
</body>
</html>
```